Employees at R&T Gale Power Services need new modern business cards

We need new business cards that showcase our new rebranded logo. We are seeking modern, clean, fresh, attractive cards while still being professional. We want to stand out. A little bit about us: we work in Canada and the USA. We offer Technical Field Advisors to support wind turbine manufacturers through the construction phase of wind farms. I am attaching a mock inspiration picture to lead you in the direction we want to see this go. Also, FYI We have approx. 10/11 different employees that would need their own card. Let me know when you would need everyone's name. We would love to see some black and white options as well as color copies- when using colors we want green to be the dominant color with accents for blue and orange (colors should match our logo). I have also attached copies of our old business card for reference.

Contact Information for Business Card

Name, Telephone, Email, address, company name, website. EXAMPLE: Dean Whitlock, DeanWhitlock@randtgale.net, 555-384-9162, 318276 Fallow Line #7, Marrowby, ON X9Z 4Q2, www.randtgale.net

Colors
0054AA
0677BA
7BADD7
CADEEF
E8F1F8
00AB8E
00BBA5
67D7C9
C6EFE9
E9F9F6
F0912C
F2A743
F7CA91
FBE8D2
FDF5EE

Requirements
Must have
• 2 sided business card

```html
<!DOCTYPE html>
<html lang="en">
<head>
<meta charset="utf-8">
<title>R&amp;T Gale Power Services – Business Card</title>
<link rel="stylesheet" href="https://fonts.googleapis.com/css2?family=Arimo:wght@400;700&display=swap">
<style>
  :root {
    --bg: #dcdcdc;
    --card-front: #f7f7f7;
    --card-back: #353535;
    --green: #3aaa35;
    --orange: #f0912c;
    --text: #4a4a4a;
  }
  * { margin: 0; padding: 0; box-sizing: border-box; }
  html, body { width: 1200px; height: 1200px; overflow: hidden; }
  body {
    background: var(--bg);
    font-family: "Arimo", Arial, sans-serif;
    position: relative;
  }
  .card {
    position: absolute;
    left: 262px;
    width: 686px;
    height: 392px;
    border-radius: 22px;
  }
  .card-front { top: 165px; background: var(--card-front); }
  .card-back { top: 653px; background: var(--card-back); }

  .brand-mark {
    position: absolute;
    border-radius: 50%;
    background: var(--green);
  }
  .brand-name {
    position: absolute;
    font-weight: 700;
    color: var(--green);
    text-transform: uppercase;
    letter-spacing: 0.08em;
    line-height: 1.1;
  }
  .card-front .brand-mark { left: 502px; top: 42px; width: 82px; height: 82px; }
  .card-front .brand-name { right: 42px; top: 138px; font-size: 21px; text-align: right; }
  .card-front .brand-name small { display: block; font-size: 13px; letter-spacing: 0.14em; }

  .card-back .brand-mark { left: 281px; top: 99px; width: 124px; height: 124px; }
  .card-back .brand-name { left: 0; right: 0; top: 246px; font-size: 33px; text-align: center; }
  .card-back .brand-name small { display: block; font-size: 19px; letter-spacing: 0.16em; margin-top: 2px; }

  .person-name {
    position: absolute;
    left: 52px; top: 193px;
    font-size: 22px; font-weight: 700;
    color: var(--green);
  }
  .address {
    position: absolute;
    left: 52px; top: 234px;
    font-size: 15px; line-height: 19px;
    color: var(--text);
    font-style: normal;
  }
  .contact-list {
    position: absolute;
    left: 52px; top: 285px;
    list-style: none;
    font-size: 15px; line-height: 19.5px;
    color: var(--text);
  }
  .contact-list li { display: flex; align-items: center; gap: 9px; }
  .contact-list svg { width: 14px; height: 14px; fill: var(--orange); flex: none; }
</style>
</head>
<body>
  <section class="card card-front" aria-label="Business card front">
    <span class="brand-mark" aria-hidden="true"></span>
    <div class="brand-name">R&amp;T Gale<small>Power Services</small></div>

    <h1 class="person-name">Dean Whitlock</h1>
    <address class="address">318276 Fallow Line #7<br>Marrowby, ON X9Z 4Q2</address>
    <ul class="contact-list">
      <li>
        <svg viewBox="0 0 24 24" aria-hidden="true"><path d="M6.6 10.8a15.1 15.1 0 0 0 6.6 6.6l2.2-2.2a1 1 0 0 1 1-.25 11.4 11.4 0 0 0 3.6.57 1 1 0 0 1 1 1V20a1 1 0 0 1-1 1A17 17 0 0 1 3 4a1 1 0 0 1 1-1h3.5a1 1 0 0 1 1 1c0 1.25.2 2.45.57 3.57a1 1 0 0 1-.25 1z"/></svg>
        555-384-9162
      </li>
      <li>
        <svg viewBox="0 0 24 24" aria-hidden="true"><path d="M2 5h20v14H2z M3.5 6.5 12 13l8.5-6.5" fill="none" stroke="#f0912c" stroke-width="0"/><path d="M2 5h20v2l-10 6.5L2 7z"/><path d="M2 9l10 6.5L22 9v10H2z"/></svg>
        DeanWhitlock@randtgale.net
      </li>
      <li>
        <svg viewBox="0 0 24 24" aria-hidden="true"><circle cx="12" cy="12" r="10"/><path d="M7 7c2 1 3 0 4 2s-1 3 0 5 2 3 1 5M15 5c0 2 2 2 3 4s-1 3 0 5" fill="none" stroke="#f7f7f7" stroke-width="1.6"/></svg>
        www.randtgale.net
      </li>
    </ul>
  </section>

  <section class="card card-back" aria-label="Business card back">
    <span class="brand-mark" aria-hidden="true"></span>
    <div class="brand-name">R&amp;T Gale<small>Power Services</small></div>
  </section>
</body>
</html>
```